Communications Consultancy needs Print Design Project

We are a communications consultancy providing training and services for organisations and individuals.

We have developed a Project Communication Strategy Model that is sound in functionality but poor in graphical design and structure.

We need to create a single page document that is a practical and profession tool to guide Project Managers through the process of communicating project outcomes.

The model will be used as a hard copy resource and will also need to be replicated onto a PowerPoint slide for instructional purposes.

Target Market(s)

Project Management Professionals

Industry/Entity Type

Communications

Requirements
Must have
• Icons to represent the different communication mediums (icons shown in attachment are just for example)

Enable future editing and be transfereable to PowerPoint

Have the company Logo (this can be privided as vector file etc.

Company contact details, website, phone, ABN etc.

```html
<!DOCTYPE html>
<html lang="en">
<head>
<meta charset="utf-8">
<title>Project Communication Strategy Model</title>
<link rel="stylesheet" href="https://fonts.googleapis.com/css2?family=Nunito+Sans:wght@400;700;800&family=Questrial&display=swap">
<style>
  :root {
    --backdrop: #efefef;
    --page: #ffffff;
    --panel: #58585a;
    --sheet: #ffffff;
    --lime: #9ad61e;
    --lime-dark: #7fb80f;
    --ink: #1d1d1d;
    --strip: #d9dbdc;
    --pill-light: #ffffff;
    --pill-dark: #111111;
    --orange: #f26522;
    --green-mail: #6cc431;
  }
  * { box-sizing: border-box; margin: 0; padding: 0; }
  html, body { width: 1200px; height: 841px; overflow: hidden; }
  body {
    background: var(--backdrop);
    font-family: "Nunito Sans", Arial, sans-serif;
    color: var(--ink);
    position: relative;
  }
  .page {
    position: absolute; left: 53px; top: 36px; width: 1102px; height: 770px;
    background: var(--page);
    box-shadow: 0 0 14px rgba(0,0,0,.18);
  }
  .panel {
    position: absolute; left: 113px; top: 73px; width: 983px; height: 694px;
    background: var(--panel);
  }
  .model-title {
    position: absolute; left: 135px; top: 108px;
    font-size: 23px; font-weight: 800; color: var(--lime);
  }
  .brand {
    position: absolute; left: 768px; top: 88px; width: 296px; text-align: right;
    font-family: "Questrial", Arial, sans-serif; color: #2a2a2a;
    font-size: 34px; line-height: 1;
  }
  .brand span { display: block; font-size: 17px; margin-top: 6px; }
  .sheet {
    position: absolute; left: 119px; top: 163px; width: 970px; height: 593px;
    background: var(--sheet); border-radius: 12px;
  }
  .connectors { position: absolute; left: 0; top: 0; width: 1200px; height: 841px; }
  .pill {
    position: absolute; height: 20px;
    background: linear-gradient(90deg, var(--pill-light) 0%, #bdbdbd 45%, var(--pill-dark) 100%);
    border: 2px solid var(--lime); border-radius: 4px;
    font-size: 11.5px; font-weight: 700; color: var(--ink);
    display: flex; align-items: center; justify-content: center;
    letter-spacing: .2px;
  }
  .pill--tall { height: 23px; }
  .event {
    position: absolute; left: 131px; top: 179px; width: 142px; height: 120px;
    border: 2px solid var(--lime); border-radius: 6px;
    background: linear-gradient(90deg, #ffffff 0%, #a7a7a7 55%, #141414 100%);
    display: flex; align-items: center; justify-content: center;
    font-size: 26px; font-weight: 800; letter-spacing: .5px;
  }
  .audience {
    position: absolute; left: 128px; width: 144px; height: 79px;
    border: 2px solid var(--lime); border-radius: 6px;
    background: linear-gradient(90deg, #ffffff 0%, #a7a7a7 55%, #141414 100%);
    display: flex; align-items: center; justify-content: center;
    font-size: 12.5px; font-weight: 700;
  }
  .checklist {
    position: absolute; left: 293px; list-style: none;
    font-size: 11px; line-height: 16.3px; color: #333;
  }
  .media-strip {
    position: absolute; left: 640px; top: 219px; width: 443px; height: 72px;
    background: var(--strip);
  }
  .techniques {
    position: absolute; top: 383px; font-size: 12.5px; font-weight: 700; color: var(--lime);
  }
  .stage {
    position: absolute; top: 707px; width: 131px; height: 37px;
    border: 3px solid var(--lime); border-radius: 6px; background: #fff;
    display: flex; align-items: center; justify-content: center;
    font-size: 20px; font-weight: 800; color: var(--lime);
  }
</style>
</head>
<body>
  <div class="page"></div>
  <div class="panel"></div>
  <h1 class="model-title">Project Communication Strategy Model</h1>
  <div class="brand">northgate<span>communications</span></div>
  <div class="sheet"></div>

  <svg class="connectors" viewBox="0 0 1200 841" aria-hidden="true">
    <g fill="none" stroke="#9ad61e" stroke-width="2">
      <line x1="273" y1="240" x2="298" y2="240"/>
      <line x1="370" y1="211" x2="370" y2="267"/>
      <line x1="444" y1="201" x2="459" y2="201"/>
      <polyline points="444,276 462,276 462,323 188,323 188,408"/>
    </g>
    <polygon points="178,405 198,405 188,421" fill="#9ad61e"/>
  </svg>

  <div class="event">EVENT</div>
  <div class="pill" style="left:298px;top:191px;width:146px;">NO</div>
  <div class="pill" style="left:459px;top:191px;width:147px;">END</div>
  <div class="pill" style="left:298px;top:230px;width:146px;">REPORTABLE?</div>
  <div class="pill" style="left:298px;top:267px;width:146px;">YES</div>
  <div class="pill" style="left:126px;top:342px;width:146px;">CHANNEL</div>

  <div class="pill" style="left:640px;top:191px;width:445px;">MEDIUM</div>
  <svg class="media-strip" viewBox="0 0 443 72" role="img" aria-label="Communication medium icons: email, mobile phone, contact card, laptop, speaker, meeting">
    <rect x="10" y="12" width="62" height="48" rx="4" fill="#fff"/>
    <rect x="18" y="20" width="46" height="32" fill="#6cc431"/>
    <polyline points="18,20 41,39 64,20" fill="none" stroke="#fff" stroke-width="3"/>
    <line x1="18" y1="52" x2="34" y2="36" stroke="#fff" stroke-width="2"/>
    <line x1="64" y1="52" x2="48" y2="36" stroke="#fff" stroke-width="2"/>
    <rect x="95" y="12" width="30" height="50" rx="4" fill="#fff"/>
    <rect x="100" y="17" width="20" height="40" rx="3" fill="#6cc431"/>
    <rect x="103" y="21" width="14" height="11" fill="#fff"/>
    <g fill="#fff"><rect x="103" y="36" width="3" height="3"/><rect x="108.5" y="36" width="3" height="3"/><rect x="114" y="36" width="3" height="3"/><rect x="103" y="42" width="3" height="3"/><rect x="108.5" y="42" width="3" height="3"/><rect x="114" y="42" width="3" height="3"/><rect x="103" y="48" width="3" height="3"/><rect x="108.5" y="48" width="3" height="3"/><rect x="114" y="48" width="3" height="3"/></g>
    <rect x="148" y="14" width="62" height="46" rx="6" fill="#fff"/>
    <rect x="153" y="19" width="52" height="36" rx="5" fill="#3d3d3f"/>
    <rect x="160" y="27" width="14" height="18" fill="#fff"/>
    <g stroke="#fff" stroke-width="3"><line x1="179" y1="29" x2="199" y2="29"/><line x1="179" y1="36" x2="199" y2="36"/><line x1="179" y1="43" x2="199" y2="43"/></g>
    <rect x="230" y="10" width="60" height="52" rx="5" fill="#fff"/>
    <rect x="236" y="16" width="48" height="32" rx="2" fill="#f26522"/>
    <rect x="240" y="20" width="40" height="24" fill="#fff"/>
    <rect x="232" y="49" width="56" height="7" rx="2" fill="#f26522"/>
    <rect x="308" y="10" width="58" height="52" rx="5" fill="#fff"/>
    <rect x="328" y="16" width="32" height="20" rx="3" fill="#f26522"/>
    <polygon points="334,36 342,36 332,44" fill="#f26522"/>
    <rect x="314" y="40" width="22" height="16" rx="6" fill="#f26522"/>
    <rect x="380" y="8" width="60" height="56" fill="#c9cbcc"/>
  </svg>

  <div class="pill pill--tall" style="left:637px;top:319px;width:445px;">DELIVERY</div>
  <div class="pill pill--tall" style="left:637px;top:347px;width:335px;">INFLUENCING TECHNIQUE</div>
  <div class="pill pill--tall" style="left:984px;top:347px;width:96px;">PRIORITY</div>
  <span class="techniques" style="left:637px;">Rational</span>
  <span class="techniques" style="left:716px;">Emotional</span>
  <span class="techniques" style="left:805px;">Consultation</span>
  <span class="techniques" style="left:912px;">Collaboration</span>
  <span class="techniques" style="left:1027px;">Medium</span>

  <div class="audience" style="top:427px;">Management</div>
  <ol class="checklist" style="top:426px;">
    <li>1....................................</li><li>2....................................</li><li>3....................................</li><li>4....................................</li><li>5....................................</li>
  </ol>
  <div class="audience" style="top:521px;">Stakeholders</div>
  <ol class="checklist" style="top:519px;">
    <li>1....................................</li><li>2....................................</li><li>3....................................</li><li>4....................................</li><li>5....................................</li>
  </ol>
  <div class="audience" style="top:613px;">Project Team</div>
  <ol class="checklist" style="top:611px;">
    <li>1....................................</li><li>2....................................</li><li>3....................................</li><li>4....................................</li><li>5....................................</li>
  </ol>

  <div class="stage" style="left:172px;">Who</div>
  <div class="stage" style="left:416px;">What</div>
  <div class="stage" style="left:662px;">How</div>
  <div class="stage" style="left:917px;">When</div>
</body>
</html>
```